Start-up Cleaning Business Needs Professional Business Cards

Marisol's Butler Tidying, LLC, is a start-up business based in the Northern Virginia suburbs of Washington, DC. MBT provides cleaning and housekeeping services for homes and offices. We have three core values:

1. We are personal. We value knowing and being known by our customers and each other. If you want nameless, faceless service, you should choose another provider. We put "personal" at the front of the list, because it is most important to us; the design we choose will convey this value.

2. Like a hotel concierge, we are professional in attitude, posture, communication and processes.

3. Like a hotel concierge, we solve problems with a can-do attitude and never make excuses.

Our uniforms are khaki pants with pink polo shirts.

Our logo is attached. There are other symbols, not represented in our logo, that may convey our values well, such as a top hat and bow tie, magnifying glass, desk bell, etc.

Please include fields for an individual's name and title, office phone number, mobile phone number, email address and website address (www.marisolsbutlertidying-example.com).

Standard U.S. size: 2" x 3.5"
Updates

I should have mentioned that the purpose of all our advertising - business cards included - is to motivate potential customers to call or email to arrange a free in-home estimate.

```html
<!DOCTYPE html>
<html lang="en">
<head>
<meta charset="utf-8">
<title>Marisol's Butler Tidying – Business Card</title>
<link href="https://fonts.googleapis.com/css2?family=Figtree:wght@400;500&family=Michroma&display=swap" rel="stylesheet">
<style>
  :root {
    --canvas: #bebebe;
    --card-front: #3d0f10;
    --card-back: #ffffff;
    --ink-light: #ffffff;
    --ink-dark: #3a3a3a;
    --deco: #5e3330;
    --art-pink: #e7b3cd;
    --art-rose: #f3e4ea;
  }
  html, body {
    margin: 0;
    padding: 0;
    width: 1200px;
    height: 1000px;
    overflow: hidden;
    background: var(--canvas);
  }
  .canvas {
    position: relative;
    width: 1200px;
    height: 1000px;
  }
  .card-front {
    position: absolute;
    left: 124px;
    top: 302px;
    width: 543px;
    height: 318px;
    background: var(--card-front);
    color: var(--ink-light);
    font-family: "Figtree", sans-serif;
    overflow: hidden;
  }
  .holder-name {
    position: absolute;
    left: 263px;
    top: 39px;
    margin: 0;
    font-family: "Michroma", sans-serif;
    font-size: 24px;
    font-weight: 400;
    letter-spacing: 0.6px;
    white-space: nowrap;
  }
  .holder-title {
    position: absolute;
    left: 262px;
    top: 76px;
    margin: 0;
    font-size: 14.5px;
  }
  .contact-list {
    position: absolute;
    left: 52px;
    top: 173px;
    margin: 0;
    padding: 0;
    list-style: none;
    font-size: 14.5px;
    line-height: 17px;
  }
  .contact-list li {
    display: flex;
    align-items: flex-start;
    margin-bottom: 4px;
    white-space: nowrap;
  }
  .contact-list .email { margin-bottom: 6px; }
  .contact-list svg {
    flex: none;
    width: 13px;
    height: 13px;
    margin: 2px 8px 0 0;
  }
  .deco-emblem {
    position: absolute;
    left: 350px;
    top: 145px;
    width: 185px;
    height: 165px;
    background: radial-gradient(closest-side, rgba(94,51,48,0.95) 0%, rgba(94,51,48,0.6) 55%, rgba(94,51,48,0) 100%);
  }
  .card-back {
    position: absolute;
    left: 769px;
    top: 153px;
    width: 318px;
    height: 543px;
    background: var(--card-back);
  }
  .mascot-art {
    position: absolute;
    left: 46px;
    top: 48px;
    width: 226px;
    height: 350px;
    background: linear-gradient(160deg, var(--art-rose) 0%, var(--art-pink) 100%);
    border-radius: 6px;
  }
  .brand-name {
    position: absolute;
    left: 0;
    top: 410px;
    width: 318px;
    margin: 0;
    text-align: center;
    font-family: "Figtree", sans-serif;
    font-weight: 400;
    font-size: 30px;
    line-height: 38px;
    color: var(--ink-dark);
  }
</style>
</head>
<body>
<main class="canvas">
  <section class="card-front">
    <div class="deco-emblem" role="img" aria-label="Faint decorative emblem of a top hat, bow tie and magnifying glass"></div>
    <h1 class="holder-name">Corwen Pell</h1>
    <p class="holder-title">CEO / Founder</p>
    <ul class="contact-list">
      <li>
        <svg viewBox="0 0 13 13"><rect width="13" height="13" rx="2" fill="#fff"/><path d="M4 3.2c.5-.4 1-.3 1.2.2l.5 1.2c.1.3 0 .6-.2.8l-.4.3c.4.9 1 1.5 1.9 1.9l.3-.4c.2-.2.5-.3.8-.2l1.2.5c.5.2.6.7.2 1.2l-.6.6C7 9.6 3.4 6 3.4 3.8z" fill="#3d0f10"/></svg>
        +1 555.014.2277
      </li>
      <li class="email">
        <svg viewBox="0 0 13 13"><rect width="13" height="13" rx="2" fill="#fff"/><rect x="3" y="4.5" width="7" height="5" fill="none" stroke="#3d0f10" stroke-width="1"/><path d="M3 4.5l3.5 2.8L10 4.5" fill="none" stroke="#3d0f10" stroke-width="1"/></svg>
        hello@mbt-example.com
      </li>
      <li>
        <svg viewBox="0 0 13 13"><rect width="13" height="13" rx="2" fill="#fff"/><circle cx="6.5" cy="6.5" r="3.6" fill="none" stroke="#3d0f10" stroke-width="0.9"/><path d="M2.9 6.5h7.2M6.5 2.9c-1.6 2-1.6 5.2 0 7.2M6.5 2.9c1.6 2 1.6 5.2 0 7.2" fill="none" stroke="#3d0f10" stroke-width="0.8"/></svg>
        www.marisolsbutlertidying-example.com
      </li>
      <li>
        <svg viewBox="0 0 13 13"><rect width="13" height="13" rx="2" fill="#fff"/><path d="M6.5 2.5a2.8 2.8 0 0 1 2.8 2.8c0 2-2.8 5.2-2.8 5.2S3.7 7.3 3.7 5.3a2.8 2.8 0 0 1 2.8-2.8z" fill="#3d0f10"/><circle cx="6.5" cy="5.3" r="1" fill="#fff"/></svg>
        <span>PO Box 000 0000 Harbor Lane<br>Brookfield VA 0000 USA</span>
      </li>
    </ul>
  </section>

  <section class="card-back">
    <div class="mascot-art" role="img" aria-label="Sketch-style illustration of a housekeeper in a pink uniform mopping the floor"></div>
    <p class="brand-name">Marisol's<br>Butler Tidying</p>
  </section>
</main>
</body>
</html>
```